CREATE A 2 layout and logo ( velunarix )

I need to create 2 layout for my company being a homepage will be like and other client control panel and need to create the logo of the company, my company works with website hosting and sale of dedicated server and VPS cloud the company name and velunarix, I want the site to be very accessible and that is not too flashy

Target Market(s)

website hosting

Industry/Entity Type

It Company

Number of Pages Required

2 page

Font styles to use
Sans Serif

Requirements
Must have
• domain velunarix.example
Nice to have
• banners, login area, login webmail
Should not have
• no preference

```html
<!DOCTYPE html>
<html lang="en">
<head>
<meta charset="utf-8">
<title>velunarix.example — Reliable Web Hosting</title>
<link href="https://fonts.googleapis.com/css2?family=Lato:wght@300;400;700;900&display=swap" rel="stylesheet">
<style>
:root{
  --teal:#1fc0c4;
  --orange:#ff9a2e;
  --blue:#3399f2;
  --red:#dc0a0a;
  --ink:#444;
  --muted:#8f9a9c;
  --line:#dedede;
  --topbar:#3b3b3b;
  --footer:#3a3a3a;
  --footer-band:#303030;
  --footer-base:#262626;
}
*{box-sizing:border-box;margin:0;padding:0}
html,body{width:1200px;height:2315px;overflow:hidden}
body{position:relative;background:#fff;font-family:"Lato",sans-serif;color:var(--ink)}
h1,h2,h3,h4{font-weight:400}
.abs{position:absolute}
ul{list-style:none}
.tick{position:relative;padding-left:24px}
.tick::before{content:"";position:absolute;left:4px;top:3px;width:6px;height:11px;border:solid var(--c,var(--teal));border-width:0 2px 2px 0;transform:rotate(40deg)}

/* top bar */
.topbar{left:0;top:0;width:1200px;height:30px;background:var(--topbar)}
.social{left:222px;top:10px;display:flex;gap:14px}
.social span{width:10px;height:10px;border-radius:50%;background:#888}
.toplinks{right:162px;top:0;display:flex;height:30px;align-items:center;font-size:13px;color:#eee}
.toplinks a{padding:0 15px;border-left:1px solid #666;color:#eee;text-decoration:none}
.toplinks a:first-child{border:0}

/* header */
.header{left:0;top:30px;width:1200px;height:72px;background:#fff;border-bottom:1px solid #eee}
.logo{left:180px;top:53px;font-size:23px;line-height:26px;font-weight:400;color:var(--teal);letter-spacing:.5px}
.nav{left:486px;top:58px;display:flex;font-size:13.5px}
.nav a{padding:0 16px;border-left:1px solid #ddd;color:#555;text-decoration:none;line-height:16px}
.nav a:first-child{border:0;color:var(--teal)}

/* hero */
.hero{left:0;top:102px;width:1200px;height:480px;background:linear-gradient(#fff,#f6f6f6)}
.hero-title{left:180px;top:150px;font-size:35px;line-height:40px;font-weight:900;color:var(--teal);letter-spacing:.5px}
.hero-sub{left:180px;top:198px;font-size:15px;color:#444;letter-spacing:.3px}
.hero-list{left:180px;top:248px;font-size:13.5px;color:var(--muted);line-height:26.5px}
.btn{display:inline-block;font-size:12.5px;text-transform:uppercase;padding:0 13px;height:33px;line-height:31px}
.btn-ghost{left:183px;top:484px;border:1px solid #ccc;background:#fff;color:#555}
.btn-teal{left:295px;top:484px;background:var(--teal);color:#fff;border:1px solid #16a5a8;padding:0 20px}
.promo-note{left:480px;top:427px;font-size:13px;color:var(--teal)}
.price-badge{left:484px;top:451px;width:104px;height:104px;border-radius:50%;background:#fff;box-shadow:0 2px 8px rgba(0,0,0,.2);text-align:center}
.price-badge small{display:block;margin-top:22px;font-size:11px;color:#999}
.price-badge b{display:block;font-size:23px;font-weight:400;color:var(--teal)}
.price-badge i{font-style:normal;font-size:10px;color:#999}
.hero-art{left:722px;top:164px;width:312px;height:320px;border-radius:14px;background:linear-gradient(135deg,#4a4a4a,#111 60%,#555)}
.slide-arrow{top:302px;width:36px;height:38px;border:1px solid #ccc;background:#fff}
.slide-arrow svg{display:block;margin:12px auto}

/* intro */
.intro{left:190px;top:606px;width:820px;text-align:center;font-size:14px;line-height:20px;color:#555;text-transform:uppercase}
.dash{left:0;top:680px;width:1200px;border-top:1px dashed #ccc}

/* pricing */
.plan{top:752px;width:219px;height:376px;border:1px solid var(--line);background:#fff}
.plan-head{height:35px;line-height:35px;background:#555;color:#fff;text-align:center;font-size:15px;text-transform:uppercase}
.plan-price{height:72px;background:var(--c);clip-path:polygon(0 0,100% 0,100% 60%,50% 100%,0 60%);text-align:center;color:#fff}
.plan-price b{display:block;padding-top:6px;font-size:25px;font-weight:900}
.plan-price span{font-size:10px;display:block;margin-top:-3px}
.plan ul{margin:20px 14px 0 16px;font-size:10.5px;color:#777}
.plan li{height:28.5px;line-height:28px;border-bottom:1px dotted #ddd;padding-left:20px}
.plan li::before{top:8px;left:3px;width:4px;height:8px}
.plan-btn{display:block;margin:22px auto 0;width:112px;height:32px;line-height:32px;background:var(--c);color:#fff;text-align:center;font-size:11px;font-weight:700;text-transform:uppercase}

/* features */
.features{left:0;top:1192px;width:1200px;height:336px;background:linear-gradient(#fbfbfb,#f3f3f3)}
.feat-title{top:1222px;font-size:16px;color:#444;text-transform:uppercase}
.card{top:1258px;height:240px;background:#fff;box-shadow:0 1px 4px rgba(0,0,0,.12)}
.card ul{padding:22px 0 0 22px;font-size:14px;line-height:27.5px;color:#444}
.service{left:743px;width:284px;height:76px;background:#fff;box-shadow:0 1px 4px rgba(0,0,0,.12)}
.service .thumb{position:absolute;left:10px;top:12px;width:62px;height:52px;border-radius:4px}
.service h3{position:absolute;left:80px;top:14px;font-size:16px;text-transform:uppercase;color:#333}
.service h3 em{font-style:normal;color:var(--teal)}
.service p{position:absolute;left:80px;top:38px;font-size:14px;color:var(--muted)}

/* testimonial */
.say-title{left:0;top:1570px;width:1200px;text-align:center;font-size:20px;color:#333;text-transform:uppercase}
.quote{left:251px;top:1626px;width:708px;height:140px;border:1px dashed var(--teal);padding:28px 18px 0 50px;font-size:14px;line-height:21px;color:#555;text-align:center;background:#fff}
.quote::before{content:"\201C";position:absolute;left:50px;top:10px;font-size:34px;color:#777}
.quote-tail{left:710px;top:1764px}
.author-pic{left:713px;top:1786px;width:38px;height:38px;border-radius:50%;background:linear-gradient(#c8b8a8,#7d6c60)}
.author{left:760px;top:1797px;font-size:13px;color:#444}

/* footer */
.footer{left:0;top:1848px;width:1200px;height:293px;background:var(--footer)}
.ft-title{top:1888px;font-size:19px;color:#eee;text-transform:uppercase}
.ft-links{font-size:12px;line-height:20.7px;color:#aaa}
.ft-links li{padding-left:14px;position:relative}
.ft-links li::before{content:"";position:absolute;left:0;top:10px;width:5px;height:1px;background:#777}
.post{left:473px;width:230px;height:60px}
.post .pic{position:absolute;left:0;top:4px;width:42px;height:42px;background:linear-gradient(#9a9a9a,#5a5a5a)}
.post h4{position:absolute;left:64px;top:0;font-size:12px;color:#ccc}
.post p{position:absolute;left:64px;top:17px;font-size:10.5px;line-height:15px;color:#888}
.transfer-txt{left:826px;top:1921px;width:230px;font-size:12px;line-height:22px;color:#aaa}

.news{left:0;top:2141px;width:1200px;height:87px;background:var(--footer-band)}
.news-label{left:212px;top:2172px;font-size:14px;font-weight:700;line-height:16px;color:#eee;text-transform:uppercase}
.news-icon{left:180px;top:2173px}
.news-input{left:327px;top:2176px;width:250px;height:30px;background:#242424;border:1px solid #1c1c1c}
.news-btn{left:582px;top:2176px;width:88px;height:30px;background:var(--orange);color:#fff;font-size:12px;font-weight:700;text-align:center;line-height:30px;text-transform:uppercase}
.pay-label{left:692px;top:2170px;font-size:14px;font-weight:700;line-height:18px;color:#eee;text-transform:uppercase}
.cards{left:806px;top:2175px;display:flex;gap:10px}
.cards span{width:48px;height:30px;border-radius:3px;background:#cfcfcf}

.base{left:0;top:2228px;width:1200px;height:87px;background:var(--footer-base)}
.to-top{left:1143px;top:2217px}
.copy{left:182px;top:2269px;font-size:11px;color:#888}
.legal{left:864px;top:2269px;font-size:11px;color:#888}
</style>
</head>
<body>

<div class="abs topbar"></div>
<div class="abs social" aria-label="Social links"><span></span><span></span><span></span><span></span></div>
<nav class="abs toplinks"><a href="#">Login</a><a href="#">Help</a><a href="#">Live chat</a></nav>

<header class="abs header"></header>
<div class="abs logo">VELUNARIX.EXAMPLE</div>
<nav class="abs nav"><a href="#">HOME</a><a href="#">HOSTING</a><a href="#">FEATURES</a><a href="#">SERVICES</a><a href="#">BLOG</a><a href="#">CONTACT</a></nav>

<section class="abs hero"></section>
<a class="abs slide-arrow" style="left:-1px"><svg width="10" height="14"><path d="M8 1L2 7l6 6" fill="none" stroke="#aaa" stroke-width="1.5"/></svg></a>
<a class="abs slide-arrow" style="left:1163px"><svg width="10" height="14"><path d="M2 1l6 6-6 6" fill="none" stroke="#aaa" stroke-width="1.5"/></svg></a>
<h1 class="abs hero-title">RELIABLE WEB HOSTING</h1>
<p class="abs hero-sub">RELIABILITY PROFESSIONAL SERVICE FOR YOUR WEBSITE</p>
<ul class="abs hero-list">
  <li class="tick">Lorem ipsum dolor sit amet,</li>
  <li class="tick">Consectetuer adipiscing elit</li>
  <li class="tick">Sed diam nonummy nibh euismod</li>
  <li class="tick">Lorem ipsum dolor sit amet,</li>
  <li class="tick">Consectetuer adipiscing elit</li>
  <li class="tick">Sed diam nonummy nibh euismod</li>
  <li class="tick">Lorem ipsum dolor sit amet,</li>
  <li class="tick">Consectetuer adipiscing elit</li>
</ul>
<a class="abs btn btn-ghost">View details</a>
<a class="abs btn btn-teal">Sign up now</a>
<p class="abs promo-note">Free Domin Registration</p>
<div class="abs price-badge"><small>From only</small><b>$4.99</b><i>/m</i></div>
<div class="abs hero-art" role="img" aria-label="Illustration of two black server towers with colourful domain flags"></div>

<p class="abs intro">We have registered over 2 million domain names and host over 1.9 million websites for individuals and organizations our fasr and flexible website creator is the easy way to build &amp; manage a site for your business</p>
<div class="abs dash"></div>

<article class="abs plan" style="left:148px;--c:var(--teal)">
  <div class="plan-head">Standard plan</div>
  <div class="plan-price"><b>$2.99</b><span>per month</span></div>
  <ul><li class="tick">500 GB Disk Space</li><li class="tick">100 Databases List</li><li class="tick">Free Domin Registration</li><li class="tick">1 Hosting Space</li><li class="tick">Free Ad Coupons</li><li class="tick">Account Control panel</li><li class="tick">Free 24/7 Support</li></ul>
  <a class="plan-btn">Sign up now</a>
</article>
<article class="abs plan" style="left:378px;--c:var(--orange)">
  <div class="plan-head">Standard plan</div>
  <div class="plan-price"><b>$4.99</b><span>per month</span></div>
  <ul><li class="tick">500 GB Disk Space</li><li class="tick">100 Databases List</li><li class="tick">Free Domin Registration</li><li class="tick">1 Hosting Space</li><li class="tick">Free Ad Coupons</li><li class="tick">Account Control panel</li><li class="tick">Free 24/7 Support</li></ul>
  <a class="plan-btn">Sign up now</a>
</article>
<article class="abs plan" style="left:606px;--c:var(--blue)">
  <div class="plan-head">Standard plan</div>
  <div class="plan-price"><b>$27.99</b><span>per month</span></div>
  <ul><li class="tick">500 GB Disk Space</li><li class="tick">100 Databases List</li><li class="tick">Free Domin Registration</li><li class="tick">1 Hosting Space</li><li class="tick">Free Ad Coupons</li><li class="tick">Account Control panel</li><li class="tick">Free 24/7 Support</li></ul>
  <a class="plan-btn">Sign up now</a>
</article>
<article class="abs plan" style="left:835px;--c:var(--red)">
  <div class="plan-head">Standard plan</div>
  <div class="plan-price"><b>$99.99</b><span>per month</span></div>
  <ul><li class="tick">500 GB Disk Space</li><li class="tick">100 Databases List</li><li class="tick">Free Domin Registration</li><li class="tick">1 Hosting Space</li><li class="tick">Free Ad Coupons</li><li class="tick">Account Control panel</li><li class="tick">Free 24/7 Support</li></ul>
  <a class="plan-btn">Sign up now</a>
</article>

<section class="abs features"></section>
<h2 class="abs feat-title" style="left:153px">What's included?</h2>
<h2 class="abs feat-title" style="left:446px">Why choose us?</h2>
<h2 class="abs feat-title" style="left:743px">Our services</h2>
<div class="abs card" style="left:152px;width:278px">
  <ul><li class="tick">Free Website Builde</li><li class="tick">Free Domain Registration</li><li class="tick">Free Instant Setup!</li><li class="tick">E-Commerce Shop Carts</li><li class="tick">Free Email Accounts</li><li class="tick">$100 Searchly Advertising Offer</li><li class="tick">Hostdeck &amp; Panelo Control Panel</li></ul>
</div>
<div class="abs card" style="left:446px;width:276px;--c:var(--orange)">
  <ul><li class="tick">Domain Registration</li><li class="tick">Web Hosting Services</li><li class="tick">Reseller Web Hosting</li><li class="tick">Cloud Host Servers</li><li class="tick">Apps Installs Easy</li><li class="tick">Money Back Guarantee</li><li class="tick">Quality 24/7 Support</li></ul>
</div>
<div class="abs service" style="top:1258px"><div class="thumb" role="img" aria-label="Person with a laptop" style="background:linear-gradient(#6b8fb0,#2b3b4b)"></div><h3><em>Web site</em> hosting</h3><p>Lorem ipsum dolor sit amet,</p></div>
<div class="abs service" style="top:1339px"><div class="thumb" role="img" aria-label="Dedicated server rack" style="background:linear-gradient(#555,#1e1e1e)"></div><h3><em>Dedicated</em> server</h3><p>Lorem ipsum dolor sit amet,</p></div>
<div class="abs service" style="top:1421px"><div class="thumb" role="img" aria-label="Servers resting on a cloud" style="background:linear-gradient(#dfeef8,#8fbfe0)"></div><h3><em>VPS</em> cloud</h3><p>Lorem ipsum dolor sit amet,</p></div>

<h2 class="abs say-title">What people say's</h2>
<blockquote class="abs quote">Lorem ipsum dolor sit amet, consectetuer adipiscing elit, sed diam nonummy nibh euismod tincidunt ut laoreet dolore magna aliquam erat volutpat. Ut wisi enim ad minim veniam, quis nostrud exerci tation ullamcorper suscipit lobortis nisl ut aliquip ex ea commodo consequat.</blockquote>
<svg class="abs quote-tail" width="36" height="18"><path d="M0 1h36L18 17z" fill="#fff"/><path d="M1 1L18 17 35 1" fill="none" stroke="#1fc0c4" stroke-dasharray="3 2"/></svg>
<div class="abs author-pic" role="img" aria-label="Customer portrait"></div>
<p class="abs author">Mira Holt</p>

<footer class="abs footer"></footer>
<h3 class="abs ft-title" style="left:185px">Support/Help</h3>
<h3 class="abs ft-title" style="left:473px">Recent blog posts</h3>
<h3 class="abs ft-title" style="left:826px">Transfer your site</h3>
<ul class="abs ft-links" style="left:185px;top:1926px">
  <li>Contact Us</li><li>Knowledge Base</li><li>Downloads</li><li>My Account</li><li>Submit Ticket</li><li>Sign Up</li><li>Affiliates</li><li>Video Tutorials</li><li>Hosting Industry</li><li>News</li>
</ul>
<div class="abs post" style="top:1926px"><div class="pic" role="img" aria-label="Author photo"></div><h4>Lorem Ipsum dummy</h4><p>March 01, 2013<br>No Comments</p></div>
<div class="abs post" style="top:1998px"><div class="pic" role="img" aria-label="Author photo"></div><h4>Lorem Ipsum dummy</h4><p>March 01, 2013<br>No Comments</p></div>
<div class="abs post" style="top:2070px"><div class="pic" role="img" aria-label="Author photo"></div><h4>Lorem Ipsum dummy</h4><p>March 01, 2013<br>No Comments</p></div>
<p class="abs transfer-txt">We'll help you t make transferring your website and domain name fast and easy</p>
<ul class="abs ft-links" style="left:826px;top:1974px">
  <li>Free Website Transfer</li><li>Free Domain Transfer</li><li>Outstanding reliability</li><li>Center</li><li>Money Back</li><li>Guarantee</li><li>24/7 Support</li>
</ul>

<div class="abs news"></div>
<svg class="abs news-icon" width="22" height="16"><rect x="1" y="2" width="20" height="13" fill="none" stroke="#999" stroke-width="1.5"/><path d="M1 2l10 8 10-8" fill="none" stroke="#999" stroke-width="1.5"/></svg>
<p class="abs news-label">Newsletter<br>Sign up</p>
<div class="abs news-input"></div>
<div class="abs news-btn">Subscribe</div>
<p class="abs pay-label">Payments we<br>accept</p>
<div class="abs cards" aria-label="Accepted payment methods"><span></span><span></span><span></span><span></span><span></span></div>

<div class="abs base"></div>
<svg class="abs to-top" width="34" height="34"><circle cx="17" cy="17" r="16" fill="#222"/><path d="M17 25V10M11 16l6-6 6 6" fill="none" stroke="#fff" stroke-width="2.4"/></svg>
<p class="abs copy">Copyright © 2013 Velunarix.example. All rights reserved.</p>
<p class="abs legal">Terms of Service &nbsp;|&nbsp; Privacy Policy</p>

</body>
</html>
```